Ridgeline Journeys business card

please see website
www.ridgelinejourneys.comau

info needed on card
Kieran Folsby
Ph
email
Adventure Riding GPS trails

please use my logo and colours off my site

Industry/Entity Type

Business

Contact Information for Business Card

Kieran Folsby
kieran@ridgelinejourneys.com

```html
<!DOCTYPE html>
<html lang="en">
<head>
<meta charset="utf-8">
<title>Ridgeline Journeys – Business Card</title>
<link href="https://fonts.googleapis.com/css2?family=Open+Sans:ital,wght@0,400;0,700;0,800;1,600&display=swap" rel="stylesheet">
<style>
  :root {
    --card-yellow: #f8e71a;
    --ink-black: #111111;
    --mark-grey: #5f5f5f;
    --name-white: #ffffff;
    --tagline-ink: #1c1c1c;
    --web-yellow: #f8e71a;
  }
  html, body {
    margin: 0;
    padding: 0;
    overflow: hidden;
    background: #ffffff;
  }
  .business-card {
    position: relative;
    width: 1200px;
    height: 702px;
    overflow: hidden;
    background: var(--card-yellow);
    font-family: "Open Sans", Arial, sans-serif;
  }
  .brand {
    position: absolute;
    left: 66px;
    top: 72px;
    display: flex;
    align-items: center;
    gap: 42px;
  }
  .brand-dot {
    width: 150px;
    height: 150px;
    border-radius: 50%;
    background: var(--mark-grey);
    flex: none;
  }
  .brand-name {
    margin: 0;
    font-weight: 800;
    font-size: 44px;
    line-height: 1.05;
    letter-spacing: 1px;
    text-transform: uppercase;
    color: var(--ink-black);
  }
  .brand-tagline {
    position: absolute;
    left: 226px;
    top: 212px;
    margin: 0;
    font-style: italic;
    font-weight: 600;
    font-size: 25px;
    color: var(--tagline-ink);
  }
  .ink-band {
    position: absolute;
    left: 0;
    top: 430px;
    width: 1200px;
    height: 272px;
    background: linear-gradient(180deg, rgba(17,17,17,0) 0%, rgba(17,17,17,0.55) 22%, rgba(17,17,17,0.92) 40%, var(--ink-black) 100%);
  }
  .rider-art {
    position: absolute;
    left: 735px;
    top: 268px;
    width: 372px;
    height: 300px;
    border-radius: 46% 40% 30% 30%;
    background: radial-gradient(ellipse at 50% 55%, rgba(17,17,17,0.85) 0%, rgba(17,17,17,0.55) 55%, rgba(17,17,17,0) 75%);
  }
  .contact {
    position: absolute;
    left: 97px;
    top: 282px;
    color: var(--ink-black);
  }
  .contact-name {
    margin: 0 0 12px;
    font-weight: 700;
    font-size: 37px;
    letter-spacing: 0.5px;
    text-transform: uppercase;
    color: var(--name-white);
    text-shadow: 2px 3px 4px rgba(0,0,0,0.55);
  }
  .contact-line {
    margin: 0;
    font-size: 30px;
    line-height: 40px;
  }
  .website {
    position: absolute;
    left: 97px;
    top: 597px;
    margin: 0;
    font-size: 36px;
    color: var(--web-yellow);
  }
</style>
</head>
<body>
  <main class="business-card">
    <div class="ink-band" role="img" aria-label="Black grunge ink splash band across the bottom of the card"></div>
    <div class="rider-art" role="img" aria-label="Silhouette of a motocross rider jumping a dirt bike"></div>

    <header class="brand">
      <span class="brand-dot"></span>
      <h1 class="brand-name">Ridgeline<br>Journeys</h1>
    </header>
    <p class="brand-tagline">Adventure Riding GPS Trails</p>

    <section class="contact">
      <h2 class="contact-name">Kieran Folsby</h2>
      <p class="contact-line">+61 4127 5830</p>
      <p class="contact-line">kieran@ridgelinejourneys.com</p>
    </section>

    <p class="website">ridgelinejourneys.com.au</p>
  </main>
</body>
</html>
```